Фирменный стиль для Trelk
Визитка, Поздравительная открытка, Футболка
Всем привет!)
Мы компания которая занимается практически всем что связано с виртуальной реальностью и игровыми технологиями, а именно:
- У нас свой VR-клуб
- Магазин по продаже игровых консолей и VR систем
- Сервисный центр по ремонту оборудования (VR и консоли)
Нужно создать фирменный стиль, взяв за основу наш логотип, в первую очередь нам нужны визитка, подарочный сертификат в конверте и листовка А5.
Задача осложняется тем что у нас разнообразные сферы деятельности и нужно сделать так чтобы промо материалы можно было легко переделывать под нужную сферу, например листовку, для рекламы клуба и для рекламы магазина или сделать 3 отдельных объединенных общим лого и цветовой гаммой, как будет лучше.?
Из пожеланий хотелось бы видеть легкость и минимализм. Удачный, на наш взгляд, пример:
https://www.folioplex.net/gallery/48213906/Norvo-Rebranding
Но необязательно опираться на него, нам хотелось бы увидеть ваш свежий взгляд.
Сам логотип можно слегка подправить, пропорции, расстояния между элементами, шрифт и т.д., но в целом нужно его сохранить, можно так же добавить разделение например ниже названия писать "сервисный центр" или "магазин" для смыслового разделения на бланках и визитках.
Если будут вопросы, смело задавайте, будем стараться отвечать максимально оперативно.
Всем успехов и заранее спасибо!)

```html
<!DOCTYPE html>
<html lang="ru">
<head>
<meta charset="utf-8">
<title>Trelk — визитка</title>
<link rel="stylesheet" href="https://fonts.googleapis.com/css2?family=Montserrat:wght@300;400;500;600;700&display=swap">
<style>
  :root {
    --bg: #ecedec;
    --brand-blue: #0366fe;
    --brand-blue-light: #3384fd;
    --white: #ffffff;
    --grey-soft: #f4f4f4;
    --ink: #262626;
    --mark-grey: #c6c7c7;
    --shadow: 0 8px 28px rgba(0, 0, 0, 0.18);
  }
  * { margin: 0; padding: 0; box-sizing: border-box; }
  html, body {
    width: 1005px;
    height: 1200px;
    overflow: hidden;
    background: var(--bg);
    font-family: "Montserrat", sans-serif;
  }
  .stage { position: relative; width: 1005px; height: 1200px; }
  .card {
    position: absolute;
    left: 154px;
    width: 697px;
    height: 388px;
    overflow: hidden;
    box-shadow: var(--shadow);
  }
  .card-front { top: 112px; background: var(--brand-blue); }
  .card-back { top: 557px; background: var(--white); }
  .card-backdrop { position: absolute; inset: 0; }
  .card-front .card-backdrop {
    background: linear-gradient(150deg, var(--brand-blue) 0%, var(--brand-blue-light) 50%, var(--brand-blue) 100%);
  }
  .card-back .card-backdrop {
    background: linear-gradient(150deg, var(--white) 0%, var(--grey-soft) 50%, var(--white) 100%);
  }

  .front-name {
    position: absolute;
    left: 0; right: 0;
    top: 196px;
    text-align: center;
    font-weight: 500;
    font-size: 66px;
    line-height: 1;
    color: var(--white);
    letter-spacing: 2px;
  }

  .back-name {
    position: absolute;
    left: 91px;
    top: 76px;
    font-weight: 500;
    font-size: 56px;
    line-height: 1;
    color: var(--brand-blue);
  }
  .person-first {
    position: absolute; right: 45px; top: 84px;
    font-weight: 300; font-size: 46px; line-height: 1;
    color: var(--ink); white-space: nowrap;
  }
  .person-last {
    position: absolute; right: 45px; top: 140px;
    font-weight: 700; font-size: 49px; line-height: 1;
    color: var(--brand-blue); white-space: nowrap;
  }
  .person-role {
    position: absolute; right: 47px; top: 212px;
    font-weight: 400; font-size: 23px; line-height: 1;
    color: var(--ink); white-space: nowrap;
  }
  .contact-phone {
    position: absolute; left: 59px; top: 313px;
    font-weight: 500; font-size: 27px; line-height: 1;
    color: var(--brand-blue); white-space: nowrap;
  }
  .contact-divider {
    position: absolute; left: 348px; top: 296px;
    width: 1.5px; height: 62px;
    background: var(--brand-blue);
  }
  .contact-site {
    position: absolute; right: 45px; top: 309px;
    font-weight: 600; font-size: 32px; line-height: 1;
    color: var(--ink); white-space: nowrap;
  }

  .footer-name {
    position: absolute;
    left: 0; right: 0;
    top: 1070px;
    text-align: center;
    font-weight: 500;
    font-size: 52px;
    line-height: 1;
    color: var(--mark-grey);
    letter-spacing: 2px;
  }
</style>
</head>
<body>
<main class="stage">

  <section class="card card-front" aria-label="Лицевая сторона визитки">
    <div class="card-backdrop" role="img" aria-label="Декоративный фон из светло-синих диагональных полос"></div>
    <div class="front-name">Trelk</div>
  </section>

  <section class="card card-back" aria-label="Оборотная сторона визитки">
    <div class="card-backdrop" role="img" aria-label="Декоративный фон из светло-серых диагональных полос"></div>
    <div class="back-name">Trelk</div>
    <div class="person-first">Имя</div>
    <div class="person-last">ФАМИЛИЯ</div>
    <div class="person-role">КОНСУЛЬТАНТ</div>
    <div class="contact-phone">8 800 000 00 00</div>
    <div class="contact-divider"></div>
    <div class="contact-site">trelk.zomu</div>
  </section>

  <div class="footer-name">Trelk</div>

</main>
</body>
</html>
```